Webdesign plus CSS for a German company data register

We need a unique and attractive webdesign including CSS development for a website (https://kontorblick.de/) of our newly founded company. We collect company data from several public registers to display them aggregated.

Your design should communicate science, data security, a business note and perhaps a slice of nerdness. Elements - like color and layout - of our logo should also be found in your design.

Target Market(s)

banks, insurance companies, authorities etc.

Industry/Entity Type

Internet

Coding

Coded - Design and coding required

Number of Pages Required

3 page

Font styles to use
Sans Serif

Requirements
Must have
• mockups, CSS

eye catching, easy to read / navigate
Nice to have
• pictogramms / logos for essential content

```html
<!DOCTYPE html>
<html lang="en">
<head>
<meta charset="utf-8">
<title>Kontorblick – Company Data Register</title>
<link href="https://fonts.googleapis.com/css2?family=Poppins:wght@400;500;600;700&family=Roboto:wght@400;500&display=swap" rel="stylesheet">
<style>
:root{
  --orange:#ff6420;
  --orange-soft:#fbb9a0;
  --peach:#feece6;
  --taupe:#7d7572;
  --ink:#1e1e28;
  --text:#3a3a40;
  --footer:#f3f3f3;
  --white:#fff;
}
*{box-sizing:border-box;margin:0;padding:0}
html,body{width:1200px;height:2581px;overflow:hidden;background:var(--white)}
body{font-family:"Poppins",sans-serif;color:var(--text);position:relative}
.abs{position:absolute}
a{color:inherit;text-decoration:none}

/* Hero */
.hero{position:absolute;left:0;top:0;width:1200px;height:665px;
  background:linear-gradient(100deg,#eef0f2 0%,#dfe2e5 40%,#d5d9dd 100%)}
.hero-photo{position:absolute;left:0;top:110px;width:800px;height:555px;
  background:radial-gradient(ellipse at 55% 55%,#f0d6dc 0%,#e6e2e3 45%,rgba(222,225,228,0) 75%)}
.brand{position:absolute;left:173px;top:60px;display:flex;align-items:center;gap:10px;
  font-family:"Poppins",sans-serif;font-weight:600;font-size:20px;color:var(--orange);letter-spacing:.5px}
.brand-mark{width:18px;height:18px;background:var(--orange)}
.nav{position:absolute;left:429px;top:60px;display:flex;gap:24px;
  font-family:"Roboto",sans-serif;font-weight:500;font-size:16px;color:#2d2d33}
.nav .active{color:var(--orange);text-decoration:underline;text-underline-offset:4px}
.btn-contact{position:absolute;left:883px;top:49px;width:142px;height:44px;background:var(--orange);
  color:var(--white);font-family:"Roboto",sans-serif;font-weight:500;font-size:16px;
  display:flex;align-items:center;justify-content:center}
.hero-title{position:absolute;left:621px;top:304px;font-size:38px;font-weight:600;color:#111;letter-spacing:-.3px}
.hero-sub{position:absolute;left:621px;top:374px;font-size:26px;font-weight:500;color:#111}

.tab-band{position:absolute;left:173px;top:665px;width:852px;height:8px;background:#e5e5e5}
.tab{position:absolute;top:632px;height:72px;display:flex;align-items:center;justify-content:center;gap:12px;
  color:var(--white);font-size:20px}
.tab-persons{left:404px;width:173px;background:var(--orange)}
.tab-persons::after{content:"";position:absolute;left:78px;bottom:-9px;border:9px solid transparent;border-bottom:0;border-top-color:var(--orange)}
.tab-companies{left:586px;width:209px;background:var(--taupe)}

/* Shared section bits */
.rule{position:absolute;height:3px;background:var(--orange)}
.section-title{position:absolute;font-size:30px;font-weight:400;color:var(--ink)}
.section-title strong{font-weight:600}
.lead{position:absolute;font-size:17px;line-height:30px;color:var(--ink);letter-spacing:-.2px}

/* About */
.about-title{left:173px;top:865px}
.about-title em{font-style:normal;color:var(--orange);font-weight:600}
.about-text{left:173px;top:920px;width:420px;color:#4a4a50}
.btn-learn{position:absolute;left:173px;top:1046px;width:156px;height:48px;background:var(--taupe);color:var(--white);
  font-size:16px;display:flex;align-items:center;justify-content:center}
.about-block{position:absolute;left:745px;top:773px;width:280px;height:301px;background:var(--orange)}
.about-photo{position:absolute;left:645px;top:837px;width:280px;height:281px;
  background:linear-gradient(135deg,#eceeee 0%,#cfd2d4 35%,#2c2c30 60%,#4b4b50 100%)}

/* What we do */
.services{position:absolute;left:0;top:1220px;width:1200px;height:650px;background:var(--peach)}
.card{position:absolute;background:var(--white);border-radius:6px;box-shadow:0 2px 10px rgba(0,0,0,.05);
  display:flex;flex-direction:column;align-items:center}
.card h3{font-size:17px;font-weight:600;line-height:26px;text-align:center;color:var(--ink);margin-top:18px}
.card .read{margin-top:22px;height:34px;width:115px;background:var(--taupe);color:var(--white);font-size:13px;
  display:flex;align-items:center;justify-content:center;gap:8px}
.card-featured{background:var(--orange);border:1px solid #e65510}
.card-featured h3{color:var(--white)}
.card-featured .read{background:var(--white);color:var(--orange)}

/* Testimonials */
.avatar{position:absolute;left:566px;top:2093px;width:66px;height:66px;border-radius:50%;
  background:linear-gradient(180deg,#e8d8c5,#f4eee8);border:2px solid #f1f1f1}
.arrow{position:absolute;top:2174px;width:40px;height:40px;border-radius:50%;background:var(--orange-soft);
  display:flex;align-items:center;justify-content:center}
.quote{position:absolute;left:300px;top:2172px;width:600px;text-align:center;font-size:16px;line-height:28px;color:var(--ink)}
.quote-name{position:absolute;left:0;width:1200px;top:2240px;text-align:center;color:var(--orange);font-size:16px}

/* Footer */
.footer{position:absolute;left:0;top:2365px;width:1200px;height:216px;background:var(--footer)}
.footer-brand{position:absolute;left:490px;top:2333px;width:203px;height:100px;background:var(--white);
  box-shadow:0 3px 10px rgba(0,0,0,.07);display:flex;align-items:center;justify-content:center;gap:8px;
  color:var(--orange);font-weight:600;font-size:18px;letter-spacing:.5px}
.footer-nav{position:absolute;left:236px;top:2469px;display:flex;gap:28px;font-family:"Roboto",sans-serif;
  font-size:15px;color:#6b6b70}
.footer-nav .active{color:var(--orange);text-decoration:underline;text-underline-offset:4px}
.footer-phone{position:absolute;left:790px;top:2469px;display:flex;gap:10px;align-items:center;
  font-family:"Roboto",sans-serif;font-size:15px;color:var(--orange)}
.footer-line{position:absolute;left:232px;top:2509px;width:718px;height:1px;background:#cfcfcf}
.copyright{position:absolute;left:0;width:1200px;top:2531px;text-align:center;font-family:"Roboto",sans-serif;
  font-size:14px;color:#6b6b70}
</style>
</head>
<body>

<header class="hero">
  <div class="hero-photo" role="img" aria-label="Photo of a smiling businesswoman at a desk holding a tablet and pen next to a computer"></div>
  <div class="brand"><span class="brand-mark"></span>KONTORBLICK</div>
  <nav class="nav">
    <a class="active" href="#">Home</a><a href="#">Persons</a><a href="#">Companies</a><a href="#">Stats</a><a href="#">Data Protection</a>
  </nav>
  <a class="btn-contact" href="#">Contact Form</a>
  <h1 class="hero-title">We Keep You Covered</h1>
  <p class="hero-sub">What do you want to look for?</p>
</header>

<div class="tab-band"></div>
<div class="tab tab-persons">
  <svg width="16" height="18" viewBox="0 0 16 18" fill="none" stroke="#fff" stroke-width="1.4"><circle cx="8" cy="5" r="4"/><path d="M1 17c0-4 3-6 7-6s7 2 7 6z"/></svg>
  Persons
</div>
<div class="tab tab-companies">
  <svg width="20" height="18" viewBox="0 0 20 18" fill="none" stroke="#ddd" stroke-width="1.2"><rect x="1" y="6" width="6" height="11"/><rect x="7" y="1" width="6" height="16"/><rect x="13" y="6" width="6" height="11"/><path d="M9 4h2M9 7h2M9 10h2M3 9h2M3 12h2M15 9h2M15 12h2"/></svg>
  Companies
</div>

<section>
  <div class="rule" style="left:173px;top:834px;width:72px"></div>
  <h2 class="section-title about-title">About <em>Kontorblick</em></h2>
  <p class="lead about-text">We have made it our goal to become a reputable provider of correct commercial register data, company data and personal data.</p>
  <a class="btn-learn" href="#">Learn More</a>
  <div class="about-block"></div>
  <div class="about-photo" role="img" aria-label="Photo of a businessman in a suit typing on a laptop"></div>
</section>

<section class="services"></section>
<div class="rule" style="left:173px;top:1269px;width:64px"></div>
<h2 class="section-title" style="left:173px;top:1296px">What <strong>We Do</strong></h2>
<p class="lead" style="left:173px;top:1350px;width:680px">Our endeavors are honest and unmanipulated data about people, companies, companies and associations.</p>

<div class="card" style="left:179px;top:1463px;width:262px;height:255px;padding-top:28px">
  <svg width="70" height="66" viewBox="0 0 70 66" fill="none" stroke="var(--orange)" stroke-width="2"><rect x="22" y="6" width="44" height="58"/><rect x="36" y="2" width="16" height="8"/><path d="M32 18h28M32 24h28"/><circle cx="44" cy="38" r="6"/><path d="M34 56c0-7 4-10 10-10s10 3 10 10z"/><path d="M2 30h14l8 6v12H12L2 42z"/></svg>
  <h3>Personal Data<br>Register</h3>
  <a class="read" href="#">Read More <span>›</span></a>
</div>
<div class="card card-featured" style="left:468px;top:1432px;width:263px;height:315px;padding-top:58px">
  <svg width="70" height="66" viewBox="0 0 70 66" fill="none" stroke="#fff" stroke-width="2"><rect x="22" y="2" width="26" height="62"/><rect x="4" y="18" width="18" height="46"/><rect x="48" y="18" width="18" height="46"/><path d="M27 10h4M39 10h4M27 18h4M39 18h4M27 26h4M39 26h4M27 34h4M39 34h4M8 28h4M8 36h4M54 28h4M54 36h4"/><path d="M4 64v-8a4 4 0 0 1 8 0M14 64v-8a4 4 0 0 1 8 0M30 64v-8a5 5 0 0 1 10 0M48 64v-8a4 4 0 0 1 8 0M58 64v-8a4 4 0 0 1 8 0"/></svg>
  <h3>Companies Data<br>Register</h3>
  <a class="read" href="#">Read More <span>›</span></a>
</div>
<div class="card" style="left:758px;top:1463px;width:262px;height:255px;padding-top:28px">
  <svg width="70" height="66" viewBox="0 0 70 66" fill="none" stroke="var(--orange)" stroke-width="2"><rect x="2" y="2" width="20" height="14"/><rect x="48" y="2" width="20" height="14"/><rect x="2" y="50" width="20" height="14"/><rect x="48" y="50" width="20" height="14"/><rect x="24" y="24" width="22" height="18"/><path d="M22 9h26M22 57h26M12 16v34M58 16v34M30 36h10v6H30z"/></svg>
  <h3>Associations Data<br>Register</h3>
  <a class="read" href="#">Read More <span>›</span></a>
</div>

<section>
  <div class="rule" style="left:173px;top:1934px;width:64px"></div>
  <h2 class="section-title" style="left:173px;top:1960px">Client <strong>Testimonials</strong></h2>
  <p class="lead" style="left:173px;top:2014px">Lorem Ipsum is simply dummy text of the printing and typesetting industry</p>
  <div class="avatar" role="img" aria-label="Portrait photo of a client"></div>
  <div class="arrow" style="left:205px"><svg width="10" height="12" viewBox="0 0 10 12" fill="none" stroke="#fff" stroke-width="1.6"><path d="M7 1L2 6l5 5"/></svg></div>
  <div class="arrow" style="left:956px"><svg width="10" height="12" viewBox="0 0 10 12" fill="none" stroke="#fff" stroke-width="1.6"><path d="M3 1l5 5-5 5"/></svg></div>
  <p class="quote">Lorem Ipsum is simply dummy text of the printing and typesetting industry. Lorem Ipsum has been the industry's standard dummy text.</p>
  <p class="quote-name">Name</p>
</section>

<footer class="footer"></footer>
<div class="footer-brand"><span class="brand-mark"></span>KONTORBLICK</div>
<nav class="footer-nav">
  <a class="active" href="#">Home</a><a href="#">Persons</a><a href="#">Companies</a><a href="#">Stats</a><a href="#">Data Protection</a><a href="#">Contact Form</a>
</nav>
<div class="footer-phone">
  <svg width="14" height="18" viewBox="0 0 14 18" fill="none" stroke="#8a8a8f" stroke-width="1.4"><rect x="1" y="1" width="12" height="16" rx="2"/><path d="M5 14h4"/></svg>
  030 - 218 - 4470
</div>
<div class="footer-line"></div>
<p class="copyright">© 2020 - Kontorblick</p>

</body>
</html>
```